Web Design Project: Facility Management company

Hi! We need a new website.

Our current website: http://www.vireo-trade.ru/ and we don-t like it. =)
The structure of our company has changed and now we don't need "cleaning" and "engeneering" on this site.

We are facility management company in Russia. So we provide integrated service solutions specific to industrial services: maintenance, repair, etc. of engineering systems.
More services:
Energy planning
Automation
Audit
Statements with regulators
Video surveillance
Central heating
Security systems
Welding
Management of subcontractors
Electrical installation and service needs
Reception
Catering

Visitors:
* Managers in the field of commercial real estate
* Chief engineers
* TOP managers of large companies, malls, factories...
+ their subordinates
* Small% of applicants.

Here you can see some websites/patterns we liked:
http://www.kobalmire.ru/ (This is our competitor’s site, so our site shouldn’t be an exact copy))))
http://www.dwatqo.ru/
http://www.layoutfarrow.com/demo/24296.html
http://www.layoutfarrow.com/website-templates/10145.html

Style:
Light, hi-tech/minimalizm, the color palette should be based on the original site colors (Green + black + white). http://www.vireo-trade.ru/

Estimated sitemap:
1. Home
2. About Us
3. Company's policy
4. History + Achievements.
5. Certificates
6. Map of presence (Here you can use sample map in file "our projects")
7. Services
8. Portfolio
9. News or blog
10. Jobs
11. Contacts - with the feedback form (or the function "call to order")
12. English

Need a design pages: main page, page 404. The rest of the page could be created by general pattern.

Logo, navigation bar and contacts should be visible on all pages of a site.
Flash animation elements and buttons, etc. - not needed.

* We need to develop 3 websites, so we are looking for a long term cooperation.
Looking forward to your creativity =)

Must Have:
Clear, intuitive structure of web pages.
In the center - of pictures reflecting our main services (industrial theme). May be in rotation.
BUT! This banner (central picture) should not be a huge one =)
All relevant information should be visible at once without scrolling.

A possibility to place media files (presentations, video ...) and 2 banner links on the main page.

Font should be available in Cyrillic.
Updates

IMPORTANT!

Please notice that in thisdesign we don't need "cleaning" and "engeneering" on this site.

So don't use old block of 4pictures from our current website. We don't need it anymore. 

Thestructure of our company has changed and now we need some links (may be banners,may be something else) to our future cleaning website as well as engeneeringwebsite.
It should look like seperate (partner) companies, not like our sevices.

Regards, Vera.

Please don't forget that we need bilingual site.

So define language changing tool in your designs.

Industry/Entity Type

Industrial

```html
<!DOCTYPE html>
<html lang="en">
<head>
<meta charset="utf-8">
<title>Vireoservice — Facility Management</title>
<link href="https://fonts.googleapis.com/css2?family=Roboto:wght@300;400;500;700&display=swap" rel="stylesheet">
<style>
:root{
  --page-bg:#e6e6e6;
  --paper:#ffffff;
  --ink:#222222;
  --text:#444444;
  --muted:#5e5e5e;
  --line:#e2e2e2;
  --green:#8aa52a;
  --green-dark:#6f8c19;
  --green-soft:#d7e59c;
  --panel-head:#6b6b6b;
  --footer:#f3f3f3;
}
*{margin:0;padding:0;box-sizing:border-box}
html,body{width:1200px;height:1142px;overflow:hidden}
body{background:var(--page-bg);font-family:"Roboto",Arial,sans-serif;color:var(--text);position:relative}
.page{position:absolute;left:120px;top:0;width:960px;height:1142px;background:var(--paper)}
.abs{position:absolute}

/* header */
.brand{left:14px;top:30px;display:flex;align-items:center;gap:12px;font-size:32px;font-weight:400;letter-spacing:4px;color:var(--ink)}
.brand-mark{width:22px;height:22px;background:var(--green)}
.top-links{left:718px;top:7px;font-size:14px;color:var(--ink)}
.lang{left:872px;top:0;width:71px;height:28px;background:var(--green-soft);color:#fff;font-size:14px;text-align:center;line-height:28px}
.phone{left:716px;top:48px;display:flex;align-items:center;gap:9px;font-size:24px;color:var(--ink)}
.phone-icon{width:32px;height:32px;border-radius:5px;background:#666;display:flex;align-items:center;justify-content:center}

/* navigation */
.nav{left:0;top:109px;width:960px;height:40px;border-top:1px solid var(--line);border-bottom:1px solid var(--line);display:flex;font-size:14px;color:var(--ink)}
.nav a{color:inherit;text-decoration:none;display:flex;align-items:center;justify-content:center;border-right:1px solid var(--line);height:100%}
.nav a:last-child{border-right:none}
.nav a.active{background:#000;color:#fff;font-weight:700}

/* main column */
.banner{left:12px;top:170px;width:660px;height:250px;border-radius:6px;background:linear-gradient(90deg,#7fa6d8 0%,#a9c4e4 18%,#2c57a8 35%,#4a7fd0 65%,#8fb3e6 100%)}
.welcome{left:12px;top:445px;font-size:20px;font-weight:400;color:var(--ink)}
.welcome span{color:var(--green)}
.dots{left:14px;top:484px;list-style:none;font-size:14px;color:var(--ink)}
.dots li{height:24px;padding-left:18px;position:relative}
.dots li::before{content:"";position:absolute;left:0;top:5px;width:7px;height:7px;border-radius:50%;background:var(--green)}
.copy{left:12px;width:660px;font-size:12px;line-height:16px;color:var(--muted);text-align:justify;font-weight:300;letter-spacing:.2px}
.sub{left:13px;font-size:17px;font-weight:400;color:var(--ink)}
.lead{left:11px;top:841px;font-size:14px;font-weight:300;color:var(--muted)}
.checks{list-style:none;font-size:14px;line-height:17px;color:var(--ink)}
.checks li{position:relative;padding-left:23px;margin-bottom:7px}
.checks li svg{position:absolute;left:0;top:1px}

/* sidebar */
.services{left:698px;top:169px;width:250px;height:251px;border:1px solid #cfcfcf}
.services h3{height:36px;background:var(--panel-head);color:#fff;font-size:16px;font-weight:700;padding:9px 14px;margin:-1px -1px 0}
.services ul{list-style:none;margin-top:18px;font-size:14px;font-weight:300;line-height:17px;color:var(--muted)}
.services li{position:relative;padding-left:32px;margin-bottom:11px;padding-right:10px}
.services li svg{position:absolute;left:10px;top:3px}
.more{right:14px;bottom:11px;font-size:12px;color:var(--green);display:flex;gap:5px;align-items:center}
.video{left:698px;top:448px;width:249px;height:167px;background:linear-gradient(180deg,#f4f4f4,#d9d9d9)}
.play{left:110px;top:62px;width:36px;height:36px;border-radius:5px;background:#333}
.controls{left:0;bottom:0;width:249px;height:16px;background:#1e1e1e}
.contact-title{left:698px;top:650px;font-size:18px;font-weight:400;color:var(--ink)}
.map{left:698px;top:683px;width:248px;height:193px;background:radial-gradient(ellipse at 40% 55%,#a9e06a 0%,#b9e98a 55%,#ffffff 95%)}
.address{left:699px;top:895px;font-size:14px;line-height:17px;color:var(--ink)}
.contact-lines{left:699px;top:955px;font-size:16px;line-height:24px;color:var(--ink)}
.contact-lines span{color:var(--green)}

.footer{left:0;top:1100px;width:960px;height:42px;background:var(--footer);font-size:14px;color:var(--ink);text-align:right;padding:13px 17px 0}
</style>
</head>
<body>
<div class="page">
  <header>
    <div class="abs brand"><span class="brand-mark"></span>VIREOSERVICE</div>
    <div class="abs top-links">About us | Contact us</div>
    <div class="abs lang">Rus | Eng</div>
    <div class="abs phone">
      <span class="phone-icon"><svg width="18" height="22" viewBox="0 0 18 22"><path d="M4 1h4l1 5-3 2c1 3 3 6 6 8l2-3 4 1v4c0 2-2 3-4 3C7 20 1 12 1 5c0-2 1-4 3-4z" fill="#fff"/></svg></span>
      +7 812 555 01 47
    </div>
  </header>

  <nav class="abs nav">
    <a class="active" style="width:84px">Home</a>
    <a style="width:154px">Company's policy</a>
    <a style="width:132px">Achievements</a>
    <a style="width:109px">Certificates</a>
    <a style="width:147px">Map of presence</a>
    <a style="width:92px">Services</a>
    <a style="width:92px">Portfolio</a>
    <a style="width:74px">News</a>
    <a style="width:76px">Jobs</a>
  </nav>

  <main>
    <div class="abs banner" role="img" aria-label="Photo of a modern glass-fronted office building with a fir tree"></div>
    <h1 class="abs welcome">WELCOME TO <span>VIREOSERVICE</span></h1>
    <ul class="abs dots">
      <li>Commercial property management</li>
      <li>Complex maintenance of immovable property</li>
      <li>Commercial property maintenance service</li>
    </ul>
    <p class="abs copy" style="top:564px">These are the most important aspects of acquisition of the highest possible incomes from the commercial property object`s operation regardless of their purpose: it can be production, business center, a building of a shop, bank, restaurant, warehousing logistic complex, hotel or the biggest shopping and recreation center.</p>
    <p class="abs copy" style="top:626px">More and more modern companies – proprietors and developer companies, hand over maintenance of the buildings, structures with all installation for outsourcing to a professional management company.</p>
    <h2 class="abs sub" style="top:675px">Why do they choose us?</h2>
    <p class="abs copy" style="top:709px">Following the complex approach to management problems, we will help to optimize maintenance costs and your immovable property service.</p>
    <p class="abs copy" style="top:756px">We use an accumulated experience of immovable property maintenance, any kind of utility systems, and their modernization for extension of durability time, and you save your money.</p>
    <h2 class="abs sub" style="top:809px">What can we do?</h2>
    <p class="abs lead">Our own team of professionals will organize and provide:</p>

    <ul class="abs checks" style="left:12px;top:875px;width:315px">
      <li><svg width="15" height="15" viewBox="0 0 15 15"><rect width="15" height="15" fill="var(--green-dark)"/><path d="M3 7.5l3 3 6-6" stroke="#fff" stroke-width="2" fill="none"/></svg>Commercial property management</li>
      <li><svg width="15" height="15" viewBox="0 0 15 15"><rect width="15" height="15" fill="var(--green-dark)"/><path d="M3 7.5l3 3 6-6" stroke="#fff" stroke-width="2" fill="none"/></svg>Maintenance of immovable property</li>
      <li><svg width="15" height="15" viewBox="0 0 15 15"><rect width="15" height="15" fill="var(--green-dark)"/><path d="M3 7.5l3 3 6-6" stroke="#fff" stroke-width="2" fill="none"/></svg>Maintenance of dangerous industrial objects</li>
      <li><svg width="15" height="15" viewBox="0 0 15 15"><rect width="15" height="15" fill="var(--green-dark)"/><path d="M3 7.5l3 3 6-6" stroke="#fff" stroke-width="2" fill="none"/></svg>Maintenance and technical service of plants and factories</li>
      <li><svg width="15" height="15" viewBox="0 0 15 15"><rect width="15" height="15" fill="var(--green-dark)"/><path d="M3 7.5l3 3 6-6" stroke="#fff" stroke-width="2" fill="none"/></svg>Technical service of industrial and production equipment</li>
      <li><svg width="15" height="15" viewBox="0 0 15 15"><rect width="15" height="15" fill="var(--green-dark)"/><path d="M3 7.5l3 3 6-6" stroke="#fff" stroke-width="2" fill="none"/></svg>Technical service of automation systems and equipment of any complexity</li>
    </ul>
    <ul class="abs checks" style="left:341px;top:875px;width:330px">
      <li><svg width="15" height="15" viewBox="0 0 15 15"><rect width="15" height="15" fill="var(--green-dark)"/><path d="M3 7.5l3 3 6-6" stroke="#fff" stroke-width="2" fill="none"/></svg>Energy planning</li>
      <li><svg width="15" height="15" viewBox="0 0 15 15"><rect width="15" height="15" fill="var(--green-dark)"/><path d="M3 7.5l3 3 6-6" stroke="#fff" stroke-width="2" fill="none"/></svg>Designing and installation of security and video systems</li>
      <li><svg width="15" height="15" viewBox="0 0 15 15"><rect width="15" height="15" fill="var(--green-dark)"/><path d="M3 7.5l3 3 6-6" stroke="#fff" stroke-width="2" fill="none"/></svg>Reconstruction and modernization of central heating</li>
      <li><svg width="15" height="15" viewBox="0 0 15 15"><rect width="15" height="15" fill="var(--green-dark)"/><path d="M3 7.5l3 3 6-6" stroke="#fff" stroke-width="2" fill="none"/></svg>Outsourcing &amp; staff leasing</li>
      <li><svg width="15" height="15" viewBox="0 0 15 15"><rect width="15" height="15" fill="var(--green-dark)"/><path d="M3 7.5l3 3 6-6" stroke="#fff" stroke-width="2" fill="none"/></svg>Work with oversight bodies and government services</li>
    </ul>
  </main>

  <aside>
    <section class="abs services">
      <h3>Our Services</h3>
      <ul>
        <li><svg width="13" height="10" viewBox="0 0 13 10"><path d="M0 3h7V0l6 5-6 5V7H0z" fill="var(--green)"/></svg>Integrated Facility Management</li>
        <li><svg width="13" height="10" viewBox="0 0 13 10"><path d="M0 3h7V0l6 5-6 5V7H0z" fill="var(--green)"/></svg>Electrical Installation and Service Needs</li>
        <li><svg width="13" height="10" viewBox="0 0 13 10"><path d="M0 3h7V0l6 5-6 5V7H0z" fill="var(--green)"/></svg>Rescue Teams</li>
        <li><svg width="13" height="10" viewBox="0 0 13 10"><path d="M0 3h7V0l6 5-6 5V7H0z" fill="var(--green)"/></svg>Security Systems</li>
        <li><svg width="13" height="10" viewBox="0 0 13 10"><path d="M0 3h7V0l6 5-6 5V7H0z" fill="var(--green)"/></svg>Technical Audit</li>
      </ul>
      <div class="abs more"><svg width="13" height="10" viewBox="0 0 13 10"><path d="M0 3h7V0l6 5-6 5V7H0z" fill="var(--green)"/></svg>More Services</div>
    </section>

    <div class="abs video" role="img" aria-label="Company presentation video player">
      <div class="abs play"><svg width="36" height="36" viewBox="0 0 36 36"><path d="M13 9l14 9-14 9z" fill="#fff"/></svg></div>
      <div class="abs controls">
        <svg width="249" height="16" viewBox="0 0 249 16"><path d="M9 5l6 3-6 3z" fill="#fff"/><rect x="24" y="6" width="122" height="4" rx="2" fill="#555"/><rect x="24" y="6" width="58" height="4" rx="2" fill="var(--green)"/><rect x="194" y="6" width="30" height="4" rx="2" fill="var(--green)"/><rect x="233" y="4" width="8" height="8" fill="none" stroke="#fff"/></svg>
      </div>
    </div>

    <h3 class="abs contact-title">Contact Us</h3>
    <div class="abs map" role="img" aria-label="Map of Russia showing office locations"></div>
    <p class="abs address">Lorem ipsum dolor sit amet,<br>consectetur adipiscing elit,<br>ipsum dolor, Russia</p>
    <p class="abs contact-lines">Phone: <span>+7 812 555 01 47</span><br>Fax:&nbsp;&nbsp;&nbsp;&nbsp; <span>+7 812 555 01 47</span><br>E-mail: <span>info@lumaris-fm.ru</span></p>
  </aside>

  <footer class="abs footer">Copyright © 2010 Vireoservice. All Rights Reserved</footer>
</div>
</body>
</html>
```